TrueGrindz Complete Stationery - Logo already designed

I already have the logo designed see attached. I need have a full set of stationary and business card designed for printing. I have attached an example of what I mean.

Please feel free to be creative. Also you can use the X in the logo by its self if you think it will work.

My details:

Name: Corwin Lestak
Social media handles: @corwinlestak
W: corwinlestak.com
E: info@corwinlestak.com
​P: 08 7493 5286
PO Box 7382, Wardell Bay 6027
ABN 83 402 719 265

Target Market(s)

Anyone looking to be inspired.

Industry/Entity Type

Business

Font styles to use
Sans Serif

Colors
fbee3e
000000

Requirements
Must have
• My details:
• Name: Corwin Lestak
• Social media handles: @corwinlestak
• W: corwinlestak.com
• E: info@corwinlestak.com
• ​P: 08 7493 5286
• PO Box 7382, Wardell Bay 6027
• ABN 83 402 719 265
Nice to have
• Something a little different
Should not have
• must not look tacky.

```html
<!DOCTYPE html>
<html lang="en">
<head>
<meta charset="utf-8">
<title>TrueGrindz Stationery Set</title>
<link rel="stylesheet" href="https://fonts.googleapis.com/css2?family=Barlow+Condensed:wght@700&family=Barlow:wght@400;500&family=Source+Sans+3:wght@400;700&display=swap">
<style>
  :root {
    --backdrop: #ebebeb;
    --paper: #f4f4f4;
    --charcoal: #363636;
    --charcoal-line: #414141;
    --ink: #333333;
    --gold: #f0c419;
    --white: #ffffff;
    --sig: #dfe3ef;
  }
  * { margin: 0; padding: 0; box-sizing: border-box; }
  html, body { width: 1200px; height: 900px; overflow: hidden; }
  body { background: var(--backdrop); position: relative; font-family: "Source Sans 3", sans-serif; color: var(--ink); }

  .piece { position: absolute; }
  .piece--dark { background: var(--charcoal); color: var(--white); }

  .wordmark { position: absolute; display: flex; align-items: center; gap: 0.18em; font-family: "Barlow Condensed", sans-serif; font-weight: 700; text-transform: uppercase; line-height: 1; letter-spacing: -0.01em; white-space: nowrap; }
  .wordmark__dot { width: 0.42em; height: 0.42em; background: var(--gold); }
  .wordmark--dark { color: var(--ink); }
  .wordmark--light { color: var(--white); }

  .gold-bar { position: absolute; bottom: 0; background: var(--gold); }
  .label { color: var(--gold); }

  /* Letterhead */
  .letterhead { left: 252px; top: 112px; width: 332px; height: 470px; background: var(--paper); }
  .letterhead .wordmark { left: 24px; top: 22px; font-size: 25px; }
  .letterhead__contact { position: absolute; left: 224px; top: 21px; font-size: 5.6px; line-height: 7.2px; white-space: nowrap; }
  .letterhead__contact .po { margin-top: 3px; }
  .letterhead__recipient { position: absolute; left: 38px; top: 88px; font-size: 6.4px; line-height: 8.1px; }
  .letterhead__tick { position: absolute; left: 0; width: 8px; height: 1px; background: var(--gold); }
  .letterhead__date { position: absolute; left: 38px; top: 174px; font-size: 6.4px; }
  .letterhead__body { position: absolute; left: 38px; top: 199px; width: 272px; font-size: 6.2px; line-height: 9px; }
  .letterhead__body .salute { font-weight: 700; margin-bottom: 8px; }
  .letterhead__body p { margin-bottom: 9px; }
  .letterhead__signature { position: absolute; left: 36px; top: 378px; width: 56px; height: 22px; background: var(--sig); border-radius: 3px; }
  .letterhead__signer { position: absolute; left: 38px; top: 406px; font-size: 5.2px; }
  .letterhead .gold-bar { left: 224px; width: 84px; height: 8px; font-size: 5.2px; color: var(--ink); text-align: center; line-height: 8px; font-weight: 700; }

  /* Presentation folder */
  .folder { left: 640px; top: 90px; width: 392px; height: 494px; }
  .folder__spine { position: absolute; top: 0; bottom: 0; width: 1px; background: var(--charcoal-line); }
  .folder .wordmark { left: 25px; top: 446px; font-size: 24px; }
  .folder .gold-bar { left: 25px; width: 104px; height: 8px; }
  .folder__handle { position: absolute; right: 24px; top: 463px; font-family: "Barlow", sans-serif; font-size: 7.6px; }

  /* Business cards */
  .card { left: 132px; width: 150px; height: 85px; }
  .card--front { top: 623px; }
  .card--back { top: 732px; }
  .card .wordmark { left: 13px; font-size: 13px; }
  .card--front .wordmark { top: 59px; }
  .card--back .wordmark { top: 37px; }
  .card--front .gold-bar { left: 13px; width: 52px; height: 5px; }
  .card__handle { position: absolute; left: 86px; top: 64px; font-family: "Barlow", sans-serif; font-size: 4.6px; }
  .card__name { position: absolute; left: 78px; top: 22px; font-family: "Barlow", sans-serif; font-weight: 500; font-size: 5.6px; color: var(--gold); }
  .card__details { position: absolute; left: 78px; top: 35px; font-family: "Barlow", sans-serif; font-size: 3.9px; line-height: 5.4px; white-space: nowrap; }
  .card__details .gap { margin-top: 2px; }

  /* Envelopes */
  .envelope { top: 636px; width: 372px; height: 177px; }
  .envelope--front { left: 321px; }
  .envelope--back { left: 728px; }
  .envelope--front .wordmark { left: 27px; top: 22px; font-size: 19px; }
  .envelope__return { position: absolute; left: 16px; bottom: 17px; font-family: "Barlow", sans-serif; font-size: 7px; }
  .envelope--front .gold-bar { left: 17px; width: 100px; height: 7px; }
  .envelope--back .wordmark { left: 50%; transform: translateX(-50%); top: 27px; font-size: 16px; }
  .envelope__flap { position: absolute; left: 0; top: 0; }
</style>
</head>
<body>

  <section class="piece letterhead" aria-label="Letterhead">
    <div class="wordmark wordmark--dark"><span>TrueGrindz</span><span class="wordmark__dot"></span></div>
    <div class="letterhead__contact">
      <div><span class="label">P</span> : 08 7493 5286</div>
      <div><span class="label">E</span> : info@corwinlestak.com</div>
      <div><span class="label">W</span> : corwinlestak.com</div>
      <div class="po">PO Box 7382, Wardell Bay 6027</div>
    </div>
    <div class="letterhead__recipient">
      Vandrel GmbH<br>Lenz Aubrecht<br>Morvenstrasse 24<br>4058 Basel<br>Schweiz
    </div>
    <div class="letterhead__tick" style="top:156px"></div>
    <div class="letterhead__tick" style="top:312px"></div>
    <div class="letterhead__date">Wardell Bay, March 26, 2016</div>
    <div class="letterhead__body">
      <div class="salute">Lorem Ipsum,</div>
      <p>Cras mattis consectetur purus sit amet fermentum. Etiam porta sem malesuada magna mollis euismod. Integer posuere erat a ante venenatis dapibus posuere velit aliquet. Cras justo odio, dapibus ac facilisis in, egestas eget quam. Aenean eu leo quam. Pellentesque ornare sem lacinia quam venenatis vestibulum.</p>
      <p>Vivamus sagittis lacus vel augue laoreet rutrum faucibus dolor auctor. Donec sed odio dui. Etiam porta sem malesuada magna mollis euismod. Morbi leo risus, porta ac consectetur ac, vestibulum at eros. Nullam id dolor id nibh ultricies vehicula ut id elit.</p>
      <p>Donec id elit non mi porta gravida at eget metus. Fusce dapibus, tellus ac cursus commodo, tortor mauris condimentum nibh, ut fermentum massa justo sit amet risus. Cras justo odio, dapibus ac facilisis in, egestas eget quam. Cum sociis natoque penatibus et magnis dis parturient montes, nascetur ridiculus mus.</p>
      <p>Cum sociis natoque penatibus et magnis dis parturient montes, nascetur ridiculus mus. Curabitur blandit tempus porttitor. Aenean lacinia bibendum nulla sed consectetur. Lorem ipsum dolor sit amet, consectetur adipiscing elit.</p>
    </div>
    <div class="letterhead__signature" role="img" aria-label="Handwritten signature of Corwin Lestak"></div>
    <div class="letterhead__signer">Corwin Lestak</div>
    <div class="gold-bar">ABN 83 402 719 265</div>
  </section>

  <section class="piece piece--dark folder" aria-label="Presentation folder">
    <div class="folder__spine" style="left:8px"></div>
    <div class="folder__spine" style="left:13px"></div>
    <div class="wordmark wordmark--light"><span>TrueGrindz</span><span class="wordmark__dot"></span></div>
    <div class="folder__handle">@corwinlestak</div>
    <div class="gold-bar"></div>
  </section>

  <section class="piece piece--dark card card--front" aria-label="Business card front">
    <div class="wordmark wordmark--light"><span>TrueGrindz</span><span class="wordmark__dot"></span></div>
    <div class="card__handle">@corwinlestak</div>
    <div class="gold-bar"></div>
  </section>

  <section class="piece piece--dark card card--back" aria-label="Business card back">
    <div class="wordmark wordmark--light"><span>TrueGrindz</span><span class="wordmark__dot"></span></div>
    <div class="card__name">Corwin Lestak</div>
    <div class="card__details">
      <div><span class="label">P</span> : 08 7493 5286</div>
      <div><span class="label">E</span> : info@corwinlestak.com</div>
      <div><span class="label">W</span> : corwinlestak.com</div>
      <div class="gap">PO Box 7382, Wardell Bay 6027</div>
      <div class="gap">ABN 83 402 719 265</div>
    </div>
  </section>

  <section class="piece piece--dark envelope envelope--front" aria-label="Envelope front">
    <div class="wordmark wordmark--light"><span>TrueGrindz</span><span class="wordmark__dot"></span></div>
    <div class="envelope__return">PO Box 7382, Wardell Bay 6027</div>
    <div class="gold-bar"></div>
  </section>

  <section class="piece piece--dark envelope envelope--back" aria-label="Envelope back">
    <svg class="envelope__flap" width="372" height="177" viewBox="0 0 372 177" aria-hidden="true">
      <path d="M0 72 Q12 62 30 61 L342 61 Q360 62 372 44" fill="none" stroke="#444444" stroke-width="1"/>
    </svg>
    <div class="wordmark wordmark--light"><span>TrueGrindz</span><span class="wordmark__dot"></span></div>
  </section>

</body>
</html>
```